Postcard Design For House buying

I buy houses for cash that need a lot of repairs and need a post card that illustrate that, i would like one that is somehow cartoonish, I had an idea about a house and a man that was kicking to the house like you do with old cars and then he had some $ bills in his hand. This is just an idea and you should not limit yourself to that

Target Market(s)

Dallas TX (DFW)

Industry/Entity Type

Real Estate

Requirements
Must have
• A Text on the frot calling for action, like "Sell your house fast Call 512-374-9160"

```html
<!DOCTYPE html>
<html lang="en">
<head>
<meta charset="utf-8">
<title>Sell Your House Fast – Postcard</title>
<link href="https://fonts.googleapis.com/css2?family=Archivo+Black&family=Roboto:wght@400;700;900&display=swap" rel="stylesheet">
<style>
  :root{
    --page:#ffffff;
    --frame:#cfd3d8;
    --blue-deep:#0b3f8c;
    --blue-mid:#1d63c6;
    --blue-light:#2f8ee0;
    --yellow:#ffd400;
    --white:#ffffff;
    --ink:#1a1a1a;
    --green:#4caf1f;
    --phone-blue:#1f6fd1;
    --teal-line:#49b5d6;
    --stamp-line:#6fb7d6;
  }
  *{box-sizing:border-box;margin:0;padding:0}
  html,body{width:769px;height:1200px;overflow:hidden;background:var(--page)}
  body{position:relative;font-family:"Roboto",Arial,sans-serif}
  .sheet{position:absolute;inset:8px;border:1px solid var(--frame);box-shadow:0 2px 8px rgba(0,0,0,.18)}

  /* Front */
  .card-front{position:absolute;left:30px;top:25px;width:710px;height:555px;overflow:hidden;
    background:radial-gradient(ellipse at 40% 55%,var(--blue-light) 0%,var(--blue-mid) 45%,var(--blue-deep) 100%);
    border:1px solid #0a2f66}
  .card-front .swoosh{position:absolute;inset:0}
  .headline{position:absolute;left:0;right:0;top:22px;text-align:center;white-space:nowrap;
    font-family:"Archivo Black",Arial,sans-serif;font-size:44px;line-height:52px;color:var(--yellow);
    letter-spacing:.5px;text-shadow:3px 3px 0 #0a2b5e}
  .mascot{position:absolute;left:50px;top:88px;width:240px;height:440px;border-radius:20px;
    background:linear-gradient(160deg,#d9a878 0%,#2c4f8f 55%,#1b2f5c 100%)}
  .conditions{position:absolute;left:455px;top:122px;white-space:nowrap;font-family:"Archivo Black",Arial,sans-serif;
    font-size:27px;line-height:38px;color:var(--white)}
  .burst{position:absolute;left:400px;top:198px;width:285px;height:165px}
  .brand-front{position:absolute;left:400px;top:251px;width:285px;text-align:center;
    font-family:"Archivo Black",Arial,sans-serif;font-size:24px;line-height:30px;color:var(--yellow)}
  .call-front{position:absolute;left:295px;top:378px;white-space:nowrap;font-family:"Archivo Black",Arial,sans-serif;font-size:29px;line-height:36px;color:var(--yellow)}
  .phone-front{position:absolute;left:295px;top:420px;white-space:nowrap;font-family:"Archivo Black",Arial,sans-serif;font-size:50px;line-height:60px;color:var(--white)}

  /* Back */
  .card-back{position:absolute;left:30px;top:600px;width:710px;height:575px;background:var(--white);border:1px solid #d8d8d8}
  .photo-house{position:absolute;left:58px;top:24px;width:88px;height:96px;background:linear-gradient(#9aa3a8,#6b5d4f)}
  .photo-icon{position:absolute;left:338px;top:30px;width:80px;height:80px;background:linear-gradient(#c3d8a0,#7fa15b)}
  .pain-list{position:absolute;left:155px;top:22px;width:180px;text-align:center;font-size:17px;line-height:22px;font-weight:700;color:var(--ink);white-space:nowrap}
  .cta-back{position:absolute;left:95px;top:128px;white-space:nowrap;font-size:22px;font-weight:700;color:var(--ink)}
  .brand-back{position:absolute;left:45px;top:195px;display:flex;align-items:center;gap:12px;white-space:nowrap;
    font-family:"Roboto",Arial,sans-serif;font-weight:900;font-size:28px;color:var(--phone-blue)}
  .brand-back .dot{width:26px;height:26px;border-radius:50%;background:var(--green);flex:none}
  .call-back{position:absolute;left:45px;top:320px;white-space:nowrap;font-size:26px;font-weight:700;color:var(--green)}
  .phone-back{position:absolute;left:45px;top:358px;white-space:nowrap;font-size:44px;font-weight:700;color:var(--phone-blue)}
  .stamp{position:absolute;left:550px;top:22px;width:135px;height:155px;border:2px dashed var(--stamp-line)}
  .address-line{position:absolute;left:410px;width:285px;border-top:2px dashed var(--teal-line)}
</style>
</head>
<body>
<div class="sheet"></div>

<section class="card-front">
  <svg class="swoosh" viewBox="0 0 710 555" preserveAspectRatio="none" aria-hidden="true">
    <path d="M0 250 C200 180 420 330 710 210 L710 300 C430 420 220 260 0 330Z" fill="#0d3b80" opacity=".55"/>
    <path d="M0 420 C240 360 460 480 710 400 L710 555 L0 555Z" fill="#0a2f6b" opacity=".6"/>
  </svg>
  <h1 class="headline">SELL YOUR HOUSE FAST</h1>
  <div class="mascot" role="img" aria-label="Cartoon football player holding cash and a small house"></div>
  <p class="conditions">ANY CONDITION<br>ANY SITUATION</p>
  <svg class="burst" viewBox="0 0 285 165" aria-hidden="true">
    <polygon points="142,0 170,35 215,8 210,50 280,45 240,82 285,120 225,118 235,165 175,135 142,165 110,135 50,160 62,118 0,120 45,82 5,45 75,50 70,8 115,35" fill="#e3262b"/>
    <polygon points="142,18 165,48 205,28 200,62 255,60 222,85 258,115 210,112 218,148 170,125 142,148 115,125 68,143 77,112 28,113 62,85 30,60 85,62 80,28 120,48" fill="#0d3b80"/>
  </svg>
  <p class="brand-front">LONE STAR<br>CASH HOMES</p>
  <p class="call-front">Call today!</p>
  <p class="phone-front">512-374-9160</p>
</section>

<section class="card-back">
  <div class="photo-house" role="img" aria-label="Photo of a worn two-storey house"></div>
  <p class="pain-list">Tired Landlord?<br>Need to Sell Fast?<br>Inherit a Nightmare?<br>Facing Foreclosure?</p>
  <div class="photo-icon" role="img" aria-label="Illustration of a house with a green roof"></div>
  <p class="cta-back">Get Cash For Your House!</p>
  <p class="brand-back"><span class="dot"></span>Lone Star Cash Homes</p>
  <p class="call-back">Call TODAY!</p>
  <p class="phone-back">512-374-9160</p>
  <div class="stamp"></div>
  <div class="address-line" style="top:330px"></div>
  <div class="address-line" style="top:382px"></div>
  <div class="address-line" style="top:436px"></div>
  <div class="address-line" style="top:494px"></div>
</section>
</body>
</html>
```